Black Matte card with samurai logo which I would like it to be textured and company name on one side and on the other side I would like the company information with the rinzo (Face logo) Sushi logo. Double Sided card.

Target Market(s)

majority customers are University students, University sororities and fraternities.

Industry/Entity Type

It Company

Contact Information for Business Card

Rinzo Sushi
217 W. Larkmoor St
Tucson, AZ 85742
Phone (520)463-1907
Fax (520)381-5046
E-mail: Rinzosushitucson@plimvox.com
FB: Rinzosushitucson
Twitter: Rinzosushitucson

Font styles to use
Other font styles liked:
• Present Normal

```html
<!DOCTYPE html>
<html lang="en">
<head>
<meta charset="utf-8">
<title>Rinzo Sushi — Business Card</title>
<link rel="stylesheet" href="https://fonts.googleapis.com/css2?family=Lato:wght@400;700;900&display=swap">
<style>
  :root {
    --stage: #dcdcdc;
    --card-black: #231f20;
    --card-glow: #5a5a5a;
    --paper: #ffffff;
    --sushi-red: #c0392b;
    --ink: #1d1d1d;
    --text-light: #f2f2f2;
    --art-dark: #2b2b2b;
    --art-red: #a8322a;
  }
  * { box-sizing: border-box; margin: 0; padding: 0; }
  html, body {
    width: 1200px; height: 1000px; overflow: hidden;
    background: var(--stage);
    font-family: "Lato", sans-serif;
  }
  .card {
    position: absolute; left: 240px;
    width: 720px; height: 410px;
    overflow: hidden;
    box-shadow: 0 6px 18px rgba(0,0,0,.25);
  }

  /* Front side */
  .card--front {
    top: 60px;
    background: radial-gradient(ellipse 60% 65% at 50% 40%, var(--card-glow) 0%, var(--card-black) 70%);
  }
  .front__art {
    position: absolute; left: 285px; top: 70px;
    width: 150px; height: 150px;
    border-radius: 12px;
    background: radial-gradient(circle at 50% 45%, var(--art-red) 0%, var(--art-dark) 70%);
    opacity: .85;
  }
  .front__brand {
    position: absolute; left: 0; right: 0; top: 250px;
    display: flex; justify-content: center; align-items: center; gap: 14px;
  }
  .brand-dot {
    width: 18px; height: 18px; border-radius: 50%;
    background: var(--sushi-red);
  }
  .front__name {
    font-weight: 400; font-size: 48px; letter-spacing: 1px;
    color: var(--text-light);
  }

  /* Back side */
  .card--back { top: 530px; background: var(--card-black); }
  .back__top {
    position: absolute; left: 0; top: 0; width: 720px; height: 150px;
    background: var(--paper);
  }
  .back__brand {
    position: absolute; right: 30px; top: 28px;
    display: flex; align-items: center; gap: 8px;
  }
  .back__brand .brand-dot { width: 12px; height: 12px; }
  .back__name { font-weight: 900; font-size: 20px; color: var(--ink); }
  .back__email {
    position: absolute; left: 30px; top: 104px;
    display: flex; align-items: center; gap: 8px;
    font-weight: 900; font-size: 22px; color: var(--ink);
  }
  .back__twitter {
    position: absolute; left: 455px; top: 100px; width: 265px; height: 50px;
    background: var(--sushi-red); color: var(--text-light);
    font-weight: 700; font-size: 16px;
    display: flex; align-items: center; justify-content: center;
  }
  .follow-flag {
    position: absolute; left: 0; top: 160px; width: 190px; height: 48px;
    background: var(--paper);
    clip-path: polygon(0 0, 88% 0, 100% 50%, 88% 100%, 0 100%);
    display: flex; align-items: center; padding-left: 40px;
    font-weight: 700; font-size: 17px; color: var(--ink);
  }
  .back__facebook {
    position: absolute; left: 220px; top: 172px;
    font-weight: 700; font-size: 16px; color: var(--text-light);
  }
  .contact {
    position: absolute; text-align: center;
    color: var(--text-light); font-weight: 700; font-size: 18px; line-height: 1.3;
  }
  .contact svg { display: block; margin: 0 auto 8px; fill: var(--text-light); }
  .contact--fax { left: 560px; top: 168px; width: 130px; }
  .contact--phone { left: 415px; top: 212px; width: 150px; }
  .contact--address { left: 150px; top: 262px; width: 240px; }
</style>
</head>
<body>

<section class="card card--front" aria-label="Card front">
  <div class="front__art" role="img" aria-label="Samurai warrior illustration holding a sword and a fish"></div>
  <div class="front__brand">
    <span class="brand-dot"></span>
    <span class="front__name">Rinzo Sushi</span>
  </div>
</section>

<section class="card card--back" aria-label="Card back">
  <div class="back__top"></div>

  <div class="back__brand">
    <span class="brand-dot"></span>
    <span class="back__name">Rinzo Sushi</span>
  </div>

  <div class="back__email">
    <svg width="28" height="20" viewBox="0 0 28 20" aria-hidden="true">
      <rect x="1" y="1" width="26" height="18" fill="none" stroke="#1d1d1d" stroke-width="2"/>
      <polyline points="1,1 14,11 27,1" fill="none" stroke="#1d1d1d" stroke-width="2"/>
    </svg>
    Rinzosushitucson@plimvox.com
  </div>

  <div class="back__twitter">Rinzosushitucson</div>

  <div class="follow-flag">Follow on:</div>
  <div class="back__facebook">Rinzosushitucson</div>

  <div class="contact contact--fax">
    <svg width="26" height="26" viewBox="0 0 26 26" aria-hidden="true">
      <rect x="7" y="1" width="12" height="8"/>
      <rect x="2" y="10" width="22" height="14" rx="2"/>
      <rect x="6" y="14" width="3" height="3" fill="#231f20"/>
      <rect x="11" y="14" width="3" height="3" fill="#231f20"/>
      <rect x="16" y="14" width="3" height="3" fill="#231f20"/>
    </svg>
    (520)381-5046
  </div>

  <div class="contact contact--phone">
    <svg width="34" height="28" viewBox="0 0 34 28" aria-hidden="true">
      <path d="M2 10 Q17 -2 32 10 L28 14 L23 11 L23 8 Q17 6 11 8 L11 11 L6 14 Z"/>
      <path d="M8 14 L26 14 L30 27 L4 27 Z"/>
      <circle cx="17" cy="20" r="4" fill="#231f20"/>
    </svg>
    (520)463-1907
  </div>

  <div class="contact contact--address">
    <svg width="30" height="26" viewBox="0 0 30 26" aria-hidden="true">
      <path d="M15 1 L29 13 L25 13 L25 25 L18 25 L18 17 L12 17 L12 25 L5 25 L5 13 L1 13 Z"/>
    </svg>
    217 W. Larkmoor St<br>Tucson, AZ 85742
  </div>
</section>

</body>
</html>
```